Central Florida Lawn and Landscape business needs an awesome flyer design!

We are a growing lawn and landscape maintenance business looking to incorporate print mail for target advertising. This project should provide some editing capabilities for us to incorporate our logo, update any promotional offers, and adjust throughout the various seasons (lawn service, mulch jobs, one-time clean-ups, hardscape projects, etc). We'd like a clear call to action (one that we can edit if needed) to call or text today. We'll include our website address as well.
The business name is Bolden Yard Crew.
Target Market(s)
Residential homeowners
Industry/Entity Type
Lawn and landscape maintenance
Other font styles liked:
- Couture
Look and feel

```html
<!DOCTYPE html>
<html lang="en">
<head>
<meta charset="utf-8">
<title>Bolden Yard Crew – Lawn &amp; Landscape Flyer</title>
<link href="https://fonts.googleapis.com/css2?family=Poppins:wght@400;500;600;700;800&family=Oswald:wght@600&family=Dancing+Script:wght@700&display=swap" rel="stylesheet">
<style>
  :root{
    --green:#1a9a3c;
    --green-dark:#1e4d2b;
    --forest:#234f2c;
    --lime:#8fd42a;
    --yellow:#f3ef12;
    --red:#e3161b;
    --ink:#1b1b1b;
    --grey-band:#e6e6e6;
    --paper:#ffffff;
  }
  *{box-sizing:border-box;margin:0;padding:0}
  html,body{width:974px;height:1200px;overflow:hidden;background:var(--paper)}
  body{font-family:'Poppins',sans-serif;color:var(--ink)}
  .flyer{position:relative;width:974px;height:1200px;overflow:hidden;background:var(--paper)}
  .abs{position:absolute}

  .brand{left:40px;top:50px;width:290px;text-align:center}
  .brand-dot{width:70px;height:70px;border-radius:50%;background:var(--green);margin:0 auto 14px}
  .brand-name{font-weight:800;font-size:34px;line-height:1.05;color:var(--green-dark);letter-spacing:.5px}

  .headline{left:414px;top:44px}
  .headline .kicker{font-weight:800;font-size:29px;letter-spacing:11px;line-height:1}
  .headline .main{font-weight:800;font-size:51px;line-height:.88;color:var(--green);letter-spacing:-1px;margin-top:10px}
  .headline .tail{font-weight:800;font-size:23px;letter-spacing:14px;margin-top:8px;line-height:1}
  .tagline{left:418px;top:246px;font-size:14.5px;line-height:1.22;width:340px}

  .why-title{left:418px;top:310px;font-weight:700;font-size:20px}
  .why-title span,.sec-title span{color:var(--green)}
  .why-band{left:359px;top:384px;width:615px;height:120px;background:var(--grey-band);display:flex}
  .why-item{position:relative;flex:1;border-right:2px solid #fff;text-align:center;font-size:12.5px;line-height:1.25;padding-top:32px}
  .why-item:last-child{border-right:none}
  .why-icon{position:absolute;top:-25px;left:calc(50% - 23px);width:46px;height:46px;border-radius:50%;background:var(--green);border:3px solid var(--forest)}

  .photo{background:linear-gradient(160deg,#2f6b2a,#4f9a3a 55%,#7fbf4d)}
  .hero-photo{left:0;top:265px;width:359px;height:640px;border-top-right-radius:60px}
  .thumb{width:190px;height:122px;border-radius:12px;box-shadow:3px 3px 0 var(--forest)}

  .sec-title{font-weight:700;font-size:21px}
  .service-list{left:411px;top:562px;width:266px;list-style:none}
  .service-list li{font-weight:600;font-size:11.6px;height:27.5px;display:flex;align-items:center;gap:5px;border-bottom:1px dashed #9a9a9a}
  .service-list li:last-child{border-bottom:none}
  .tick{flex:none}

  .offer{top:828px;width:192px;height:204px;border-radius:18px;color:#fff;text-align:center;overflow:hidden}
  .offer-first{left:496px;background:var(--green);border:2px dashed var(--lime)}
  .offer-winter{left:703px;background:var(--forest)}
  .offer .amount{font-weight:800;font-size:38px;line-height:.85;padding:20px 8px 0 72px;text-align:left}
  .offer-winter .amount{padding-top:12px}
  .offer .label{font-weight:700;font-size:13.5px;line-height:1.1;margin-top:10px}
  .offer-winter .label{font-size:11.5px;margin-top:6px;line-height:1.15}
  .offer-winter .label .until{font-weight:400}
  .offer .foot{position:absolute;left:0;right:0;bottom:0;font-size:11.5px;line-height:1.2;padding:8px 6px}
  .offer-first .foot{background:#22a346;height:64px}
  .offer-winter .foot{background:#1a4223;height:84px;font-size:8.3px;padding-top:10px}
  .offer-winter .foot .summer{color:var(--yellow);font-weight:700;margin-top:6px}
  .badge{top:800px;width:76px;height:76px;border-radius:50%;display:flex;flex-direction:column;align-items:center;justify-content:center;font-family:'Oswald',sans-serif;font-size:19px;line-height:.95;text-transform:uppercase}
  .badge-yellow{left:484px;background:var(--yellow);color:var(--forest);border:3px dotted #fff}
  .badge-red{left:691px;background:var(--red);color:var(--yellow);border:3px dotted #fff}
  .badge .script{font-family:'Dancing Script',cursive;color:#fff;font-size:16px;text-transform:none}

  .seasonal-title{left:67px;top:918px}
  .seasonal{left:68px;top:957px;display:grid;grid-template-columns:211px 180px;font-size:12.5px;line-height:17px;white-space:nowrap}
  .seasonal div{display:flex;align-items:center;gap:8px}

  .contact-head{left:67px;top:1064px;font-weight:700;font-size:17px;letter-spacing:4px;color:var(--forest)}
  .contact-head span{color:var(--green)}
  .phone{left:67px;top:1098px;display:flex;align-items:center;gap:8px;font-weight:700;font-size:28px;color:#2b2b2b}
  .promise{left:411px;top:1062px;font-weight:700;font-size:14.5px}
  .web{left:407px;top:1096px;width:506px;height:42px;border-radius:21px;background:var(--lime);display:flex;overflow:hidden}
  .web .lead{width:126px;display:flex;align-items:center;justify-content:center;font-weight:700;font-size:15px;letter-spacing:1.5px;color:var(--forest)}
  .web .url{flex:1;background:var(--forest);border-radius:21px;display:flex;align-items:center;justify-content:center;color:#fff;font-weight:700;font-size:21px}
  .grass{left:0;top:1152px;width:974px;height:48px;background:linear-gradient(180deg,rgba(255,255,255,0),#8cc35a 45%,#4e8a2e)}
</style>
</head>
<body>
<div class="flyer">

  <div class="abs brand">
    <div class="brand-dot"></div>
    <div class="brand-name">BOLDEN YARD CREW</div>
  </div>

  <div class="abs headline">
    <div class="kicker">YOUR TRUSTED</div>
    <div class="main">LOCAL LAWN &amp;<br>LANDSCAPE</div>
    <div class="tail">EXPERTS</div>
  </div>
  <p class="abs tagline">Providing Top-Tier Lawn Care and Landscape Solutions for Every Season</p>

  <h2 class="abs why-title">Why Choose <span>Bolden Yard Crew?</span></h2>
  <div class="abs why-band">
    <div class="why-item"><div class="why-icon"></div>Reliable,<br>Professional<br>Service</div>
    <div class="why-item"><div class="why-icon"></div>Custom Lawn<br>&amp; Landscape<br>Plans</div>
    <div class="why-item"><div class="why-icon"></div>Licensed &amp;<br>Insured for<br>Your Peace<br>of Mind</div>
    <div class="why-item"><div class="why-icon"></div>Satisfaction<br>Guaranteed</div>
  </div>

  <div class="abs photo hero-photo" role="img" aria-label="Photo of a man pushing a lawn mower across a green lawn"></div>

  <h2 class="abs sec-title" style="left:411px;top:522px">Our <span>Services</span></h2>
  <ul class="abs service-list">
    <li><svg class="tick" width="11" height="10" viewBox="0 0 11 10"><path d="M1 5l3 3 6-7" fill="none" stroke="#1a9a3c" stroke-width="2.4"/></svg>LAWN CARE &amp; MAINTENANCE</li>
    <li><svg class="tick" width="11" height="10" viewBox="0 0 11 10"><path d="M1 5l3 3 6-7" fill="none" stroke="#1a9a3c" stroke-width="2.4"/></svg>REGULAR MOWING</li>
    <li><svg class="tick" width="11" height="10" viewBox="0 0 11 10"><path d="M1 5l3 3 6-7" fill="none" stroke="#1a9a3c" stroke-width="2.4"/></svg>FERTILIZATION &amp; WEED CONTROL</li>
    <li><svg class="tick" width="11" height="10" viewBox="0 0 11 10"><path d="M1 5l3 3 6-7" fill="none" stroke="#1a9a3c" stroke-width="2.4"/></svg>AERATION &amp; OVERSEEDING</li>
    <li><svg class="tick" width="11" height="10" viewBox="0 0 11 10"><path d="M1 5l3 3 6-7" fill="none" stroke="#1a9a3c" stroke-width="2.4"/></svg>LANDSCAPE &amp; GARDEN SOLUTIONS</li>
    <li><svg class="tick" width="11" height="10" viewBox="0 0 11 10"><path d="M1 5l3 3 6-7" fill="none" stroke="#1a9a3c" stroke-width="2.4"/></svg>MULCHING &amp; BED MAINTENANCE</li>
    <li><svg class="tick" width="11" height="10" viewBox="0 0 11 10"><path d="M1 5l3 3 6-7" fill="none" stroke="#1a9a3c" stroke-width="2.4"/></svg>PLANTING &amp; PRUNING</li>
    <li><svg class="tick" width="11" height="10" viewBox="0 0 11 10"><path d="M1 5l3 3 6-7" fill="none" stroke="#1a9a3c" stroke-width="2.4"/></svg>SOD INSTALLATION</li>
  </ul>
  <div class="abs photo thumb" style="left:706px;top:524px" role="img" aria-label="Photo of a mower cutting grass beside a garden bed"></div>
  <div class="abs photo thumb" style="left:706px;top:658px" role="img" aria-label="Photo of a sprayer treating a lawn"></div>

  <div class="abs offer offer-first">
    <div class="amount">20%<br>OFF</div>
    <div class="label">YOUR FIRST LAWN<br>CARE SERVICE!</div>
    <div class="foot">Call or text today to<br>schedule your<br><b>FREE CONSULTATION.</b></div>
  </div>
  <div class="abs badge badge-yellow">Special<br>Offer</div>

  <div class="abs offer offer-winter">
    <div class="amount">$100<br>OFF</div>
    <div class="label">SNOW REMOVAL SERVICE<br><span class="until">(TILL 06.05.2025)</span></div>
    <div class="foot">Fall Clean-Up Special:<br>Free Leaf Removal with<br>Any Lawn Care Package<div class="summer">Summer Ready:<br>10% Off Mulch installation</div></div>
  </div>
  <div class="abs badge badge-red"><span class="script">Winter</span>Special<br>Offer</div>

  <h2 class="abs sec-title seasonal-title">Seasonal <span>Services</span></h2>
  <div class="abs seasonal">
    <div><svg width="10" height="9" viewBox="0 0 11 10"><path d="M1 5l3 3 6-7" fill="none" stroke="#1a9a3c" stroke-width="2.4"/></svg>Leaf &amp; Debris Clean-up</div>
    <div><svg width="10" height="9" viewBox="0 0 11 10"><path d="M1 5l3 3 6-7" fill="none" stroke="#1a9a3c" stroke-width="2.4"/></svg>Patios &amp; Walkways</div>
    <div><svg width="10" height="9" viewBox="0 0 11 10"><path d="M1 5l3 3 6-7" fill="none" stroke="#1a9a3c" stroke-width="2.4"/></svg>Snow &amp; Ice Removal</div>
    <div><svg width="10" height="9" viewBox="0 0 11 10"><path d="M1 5l3 3 6-7" fill="none" stroke="#1a9a3c" stroke-width="2.4"/></svg>Retaining Walls</div>
    <div><svg width="10" height="9" viewBox="0 0 11 10"><path d="M1 5l3 3 6-7" fill="none" stroke="#1a9a3c" stroke-width="2.4"/></svg>Spring/Fall Clean-ups</div>
    <div><svg width="10" height="9" viewBox="0 0 11 10"><path d="M1 5l3 3 6-7" fill="none" stroke="#1a9a3c" stroke-width="2.4"/></svg>Outdoor Living Spaces</div>
    <div><svg width="10" height="9" viewBox="0 0 11 10"><path d="M1 5l3 3 6-7" fill="none" stroke="#1a9a3c" stroke-width="2.4"/></svg>Hardscaping Projects</div>
  </div>

  <div class="abs contact-head">CONTACT <span>US TODAY!</span></div>
  <div class="abs phone">
    <svg width="20" height="20" viewBox="0 0 20 20"><circle cx="10" cy="10" r="10" fill="#1a9a3c"/><path d="M6.5 5.5c.6-.6 1.3-.5 1.7.1l.9 1.5c.3.5.2 1-.2 1.4l-.5.5c.6 1.3 1.6 2.3 2.9 2.9l.5-.5c.4-.4.9-.5 1.4-.2l1.5.9c.6.4.7 1.1.1 1.7l-.7.7c-.7.7-2 .8-3.6-.1-2-1.1-3.6-2.7-4.7-4.7-.9-1.6-.8-2.9-.1-3.6z" fill="#fff"/></svg>
    555 0142 7788
  </div>

  <p class="abs promise">Let’s make your lawn the envy of the neighborhood!</p>
  <div class="abs web"><div class="lead">Visit us at</div><div class="url">www.boldenyardcrew.com</div></div>

  <div class="abs grass" role="img" aria-label="Strip of grass blades along the bottom edge"></div>
</div>
</body>
</html>
```